Larkmoor Counseling

We need a postcard design for a Brooklyn based counseling service geared towards new parents. The postcard will be placed in pediatrician's offices, kids stores, and any place parents frequent. We would like to see designs that incorporate elements, fonts, textures, etc from the website (www.larkmoorcounseling-example.com) and some of the basic text used to describe the business.

I've included a copy of the logo, the font file we used to create the logo, and the main image from the index of the website, and the background texture.

Target Market(s)

New parents in Brooklyn.

Industry/Entity Type

Business

Requirements
Must have
• Contact info, website.
Should not have
• This postcard is for display and promotional purposes in doctor's offices and kid's toy/clothing stores.

It does not need an area for postage / address.

```html
<!DOCTYPE html>
<html lang="en">
<head>
<meta charset="utf-8">
<title>Larkmoor Counseling – Postcard</title>
<link href="https://fonts.googleapis.com/css2?family=Amatic+SC:wght@400;700&family=Roboto+Condensed:wght@300;400&display=swap" rel="stylesheet">
<style>
  :root {
    --backdrop: #7a5232;
    --paper: #e8e4dc;
    --paper-light: #f3f1ec;
    --ink: #1f1f1f;
    --body-ink: #333130;
    --gold: #a27b3c;
    --bullet: #c08a2e;
    --footer-bg: #3c3a37;
    --footer-ink: #f4f2ee;
    --footer-accent: #e6a42c;
    --white: #ffffff;
  }
  * { box-sizing: border-box; margin: 0; padding: 0; }
  html, body { width: 800px; height: 1200px; overflow: hidden; }
  body {
    background: var(--backdrop);
    font-family: "Roboto Condensed", "Helvetica Neue", Arial, sans-serif;
    position: relative;
  }
  .card {
    position: absolute;
    left: 59px;
    width: 692px;
    background: var(--paper);
    box-shadow: 0 3px 10px rgba(0,0,0,.35);
  }

  /* Front side */
  .card--front { top: 46px; height: 534px; }
  .brand-band {
    position: absolute; left: 0; right: 0; top: 29px; height: 82px;
    background: var(--white);
    display: flex; align-items: center; justify-content: center;
  }
  .brand-name {
    font-family: "Amatic SC", "Comic Sans MS", cursive;
    font-weight: 400;
    font-size: 66px;
    letter-spacing: 2px;
    color: var(--ink);
    line-height: 1;
  }
  .hero-frame {
    position: absolute; left: 35px; top: 126px; width: 620px; height: 371px;
    background: var(--white);
    box-shadow: 0 2px 6px rgba(0,0,0,.3);
  }
  .hero-photo {
    position: absolute; inset: 8px;
    background: linear-gradient(100deg, #cfe3b0 0%, #8fae6a 22%, #7b5a4c 45%, #5d3f36 70%, #3a2724 100%);
  }
  .hero-rule {
    position: absolute; inset: 15px;
    border: 1.5px solid var(--white);
  }
  .hero-caption {
    position: absolute; left: 8px; top: 209px; width: 392px; height: 102px;
    background: rgba(255,255,255,.72);
    padding: 14px 0 0 21px;
    color: var(--ink);
  }
  .hero-caption__name { font-weight: 300; font-size: 30px; line-height: 1.05; }
  .hero-caption__line { font-weight: 300; font-size: 14px; text-transform: uppercase; line-height: 20px; }
  .hero-caption__name + .hero-caption__line { margin-top: 4px; }

  /* Back side */
  .card--back { top: 611px; height: 535px; }
  .info-panel {
    position: absolute; left: 26px; top: 21px; width: 644px; height: 422px;
    background: var(--paper-light);
    padding: 8px 20px 0 20px;
  }
  .info-title, .info-subtitle {
    font-family: "Amatic SC", "Comic Sans MS", cursive;
    color: var(--gold);
    text-align: center;
    white-space: nowrap;
  }
  .info-title { font-size: 44px; line-height: 44px; font-weight: 400; letter-spacing: 1px; }
  .info-subtitle { font-size: 30px; line-height: 34px; font-weight: 700; letter-spacing: 1px; margin-top: 4px; }
  .info-text {
    max-width: 602px;
    font-size: 16px; line-height: 21px; font-weight: 300; color: var(--body-ink);
    margin-top: 3px;
  }
  .info-subtitle + .info-text { margin-top: 6px; }
  .info-text--lead { margin-top: 6px; }
  .focus-list { list-style: none; margin-top: 2px; }
  .focus-list li {
    font-size: 16px; line-height: 25.5px; font-weight: 300; color: var(--body-ink);
    padding-left: 11px; position: relative;
  }
  .focus-list li::before {
    content: ""; position: absolute; left: 0; top: 10px;
    width: 5px; height: 5px; border-radius: 50%; background: var(--bullet);
  }
  .snapshot {
    position: absolute; background: var(--white); padding: 6px;
    box-shadow: 0 2px 5px rgba(0,0,0,.35);
  }
  .snapshot__image { width: 100%; height: 100%; }
  .snapshot--meeting { left: 304px; top: 286px; width: 148px; height: 110px; transform: rotate(7deg); }
  .snapshot--meeting .snapshot__image { background: linear-gradient(135deg, #dcdad6, #3e3c42 55%, #8c7a70); }
  .snapshot--notes { left: 467px; top: 270px; width: 146px; height: 106px; transform: rotate(5deg); }
  .snapshot--notes .snapshot__image { background: linear-gradient(135deg, #f0dcd6, #d9b4ad 50%, #f6eeec); }

  .contact-bar {
    position: absolute; left: 0; right: 0; top: 443px; height: 72px;
    background: var(--footer-bg);
    color: var(--footer-ink);
    text-align: center;
    padding-top: 9px;
  }
  .contact-row {
    display: flex; justify-content: center; gap: 16px;
    font-size: 15.5px; font-weight: 300; line-height: 22px;
  }
  .contact-item { display: inline-flex; align-items: center; gap: 4px; }
  .contact-item svg { width: 14px; height: 14px; fill: var(--footer-ink); }
  .contact-offer { color: var(--footer-accent); font-size: 17px; font-weight: 300; margin-top: 8px; }
</style>
</head>
<body>

<section class="card card--front">
  <header class="brand-band">
    <span class="brand-name">Larkmoor Counseling</span>
  </header>
  <div class="hero-frame">
    <div class="hero-photo" role="img" aria-label="Tree-lined Brooklyn street of brownstone houses with iron stoop railings"></div>
    <div class="hero-rule"></div>
    <div class="hero-caption">
      <p class="hero-caption__name">Nora Ellison, LCSW</p>
      <p class="hero-caption__line">Larkmoor Counseling</p>
      <p class="hero-caption__line">In-home therapy for parents</p>
    </div>
  </div>
</section>

<section class="card card--back">
  <div class="info-panel">
    <h1 class="info-title">Welcome to Larkmoor Counseling:</h1>
    <h2 class="info-subtitle">A comprehensive practice for new and expecting parents</h2>
    <p class="info-text">Nora Ellison is a licensed clinical social worker with years of experience working with pregnant women, new moms &amp; dads, and couples struggling through the early parenting years.</p>
    <p class="info-text">The stress of carrying for and raising children can affect each parent, as well as their relationship to each other. Nora offers individual sessions and couples therapy to work through these relationship issues.</p>
    <p class="info-text">Since getting out of the house with a newborn can often feel like a struggle, Nora will travel out-of-office to meet with parents in their home for therapy sessions.</p>
    <p class="info-text info-text--lead">Therapy may focus on:</p>
    <ul class="focus-list">
      <li>Pregnancy and postpartum depression</li>
      <li>Stress and anxiety</li>
      <li>Relationship changes</li>
      <li>Confidence building</li>
      <li>Balancing work and home life</li>
    </ul>
    <div class="snapshot snapshot--meeting"><div class="snapshot__image" role="img" aria-label="Group of people seated in a circle during a session"></div></div>
    <div class="snapshot snapshot--notes"><div class="snapshot__image" role="img" aria-label="Hand writing notes on a clipboard"></div></div>
  </div>

  <footer class="contact-bar">
    <div class="contact-row">
      <span class="contact-item">
        <svg viewBox="0 0 24 24" aria-hidden="true"><path d="M6.6 10.8a15.1 15.1 0 0 0 6.6 6.6l2.2-2.2a1 1 0 0 1 1-.25 11.4 11.4 0 0 0 3.6.57 1 1 0 0 1 1 1V20a1 1 0 0 1-1 1A17 17 0 0 1 3 4a1 1 0 0 1 1-1h3.5a1 1 0 0 1 1 1c0 1.250.2 2.45.57 3.57a1 1 0 0 1-.25 1z"/></svg>
        555.014.2290
      </span>
      <span class="contact-item">
        <svg viewBox="0 0 24 24" aria-hidden="true"><path d="M2 5h20v14H2z M4 7v.5l8 5 8-5V7z" fill-rule="evenodd"/></svg>
        nora@larkmoorcounseling-example.com
      </span>
      <span class="contact-item">
        <svg viewBox="0 0 24 24" aria-hidden="true"><path d="M12 2a10 10 0 1 0 0 20 10 10 0 0 0 0-20zm6.9 6h-2.9a15.6 15.6 0 0 0-1.4-3.6A8 8 0 0 1 18.9 8zM12 4c.8 1.2 1.5 2.5 1.9 4h-3.8c.4-1.5 1.1-2.8 1.900-4zM4.3 14a8 8 0 0 1 0-4h3.4a16 16 0 0 0 0 4zm.8 2h2.9c.3 1.3.8 2.5 1.4 3.6A8 8 0 0 1 5.1 16zM8 8H5.1a8 8 0 0 1 4.3-3.6C8.8 5.5 8.3 6.7 8 8zm4 12c-.8-1.2-1.5-2.5-1.9-4h3.8c-.4 1.5-1.1 2.8-1.9 4zm2.3-6H9.7a14.7 14.7 0 0 1 0-4h4.6a14.7 14.7 0 0 1 0 4zm.3 5.6c.6-1.1 1.1-2.3 1.4-3.6h2.9a8 8 0 0 1-4.3 3.6zm1.7-5.6a16 16 0 0 0 0-4h3.4a8 8 0 0 1 0 4z"/></svg>
        www.larkmoorcounseling-example.com
      </span>
    </div>
    <p class="contact-offer">Call for a free phone consultation • Ask about our ongoing group sessions</p>
  </footer>
</section>

</body>
</html>
```